Harbor Sushi & Steak Dinner Menu

I'm looking for a MENU design with a particular feel. I want to have a base template made that I can then use for future alterations to the menu; ie I can go in and change out different entrees as the menu changes but the template will remain the same. (Ideally it would be in an Apple Pages format.). Also ideally - dinner menu will occupy 2 pages 8.5 x 11. The restaurant's name is Harbor. It is a MODERN steak house that will also feature Sushi, a Raw Bar, Exquisite Cocktails and a sophisticated nightlife crowd. I have attached our LOGO, a secondary logo that we will be featuring throughout the project including on the menu cover (the gold U). Finally - I have attached the content that we would like to see. AGAIN - I REITERATE: High end dining and lounge atmosphere. A couple of restaurants / menus that I love are Morvendel in NYC and Pellucid Steakhouse in Long Island NY. Please do not duplicate - just trying to offer some suggestions.

Requirements
Must have
• A sophisticated and elegant feel without being stuffy or old.

```html
<!DOCTYPE html>
<html lang="en">
<head>
<meta charset="utf-8">
<title>Harbor Sushi &amp; Steak Dinner Menu</title>
<link href="https://fonts.googleapis.com/css2?family=Nunito+Sans:wght@400;500;600;800;900&display=swap" rel="stylesheet">
<style>
:root{
  --ink:#111;
  --paper:#fff;
  --shadow:#5a5a5a;
  --gold-top:#d8d39a;
  --gold-bottom:#b8744e;
  --logo-bg:#050505;
  --logo-text:#d9b46a;
}
*{margin:0;padding:0;box-sizing:border-box}
html,body{width:1200px;height:1200px;overflow:hidden;background:var(--paper)}
body{position:relative;font-family:"Nunito Sans",sans-serif;color:var(--ink);font-size:10.3px;line-height:13.7px}
.page{position:absolute;top:250px;width:543px;height:701px;background:var(--paper);border:1px solid #333;box-shadow:8px 8px 0 var(--shadow)}
.page-left{left:33px}
.page-right{left:622px}
.frame{position:absolute;border:2.5px solid var(--ink)}
.frame-left{left:61px;top:286px;width:489px;height:642px}
.frame-right{left:649px;top:286px;width:489px;height:642px}
.gap{position:absolute;background:var(--paper);height:6px;top:283px}
.brand{position:absolute;left:246px;top:258px;width:119px;height:55px;background:var(--logo-bg);display:flex;align-items:center;justify-content:center;color:var(--logo-text);font-weight:600;font-size:17px;letter-spacing:3px}
.ribbon{position:absolute;left:1062px;top:248px;width:55px;height:97px}
.orn{position:absolute;width:92px;height:9px;border-radius:5px;background:linear-gradient(90deg,transparent,#222 40%,#222 60%,transparent)}
.head{position:absolute;font-size:14px;font-weight:500;letter-spacing:0;text-align:center;white-space:nowrap;transform:translateX(-50%);line-height:18px}
.block{position:absolute;white-space:nowrap}
.block b{font-weight:800}
.hang{padding-left:32px;text-indent:-32px}
.box{position:absolute;border:2px solid var(--ink)}
.box .head{left:50%;}
.dim{font-size:9.6px;line-height:12.8px}
i.em{font-style:italic;font-weight:800}
</style>
</head>
<body>
<div class="page page-left"></div>
<div class="page page-right"></div>
<div class="frame frame-left"></div>
<div class="frame frame-right"></div>
<div class="gap" style="left:224px;width:155px"></div>
<div class="gap" style="left:1051px;width:74px"></div>

<div class="brand">HARBOR</div>
<svg class="ribbon" viewBox="0 0 55 97" aria-hidden="true">
  <defs><linearGradient id="rg" x1="0" y1="0" x2="0" y2="1"><stop offset="0" stop-color="#d8d39a"/><stop offset="1" stop-color="#b8744e"/></linearGradient></defs>
  <path d="M0 0H55V97L27.5 82L0 97Z" fill="url(#rg)"/>
</svg>

<!-- LEFT PAGE -->
<div class="orn" role="img" aria-label="leaf flourish divider" style="left:114px;top:307px"></div>
<div class="head" style="left:160px;top:320px">SUSHI / SASHIMI</div>
<div class="orn" role="img" aria-label="leaf flourish divider" style="left:114px;top:341px"></div>
<div class="block" style="left:73px;top:356px">
<b>Toro</b>&nbsp; blue fin tuna belly (gf)<br><b>Unagi</b>&nbsp; fresh water eel (gf)<br><b>Ebi</b>&nbsp; cooked shrimp (gf)<br><b>Sake</b>&nbsp; salmon (gf)<br><b>Hamachi</b>&nbsp; yellowtail (gf)<br><b>Madai</b>&nbsp; red snapper (gf)<br><b>Uni</b>&nbsp; sea urchin (gf)<br><b>Maguro</b>&nbsp; tuna (gf)<br><b>Hirame</b>&nbsp; fluke (gf)
</div>

<div class="orn" role="img" aria-label="leaf flourish divider" style="left:114px;top:495px"></div>
<div class="head" style="left:160px;top:508px">CLASSIC ROLLS</div>
<div class="orn" role="img" aria-label="leaf flourish divider" style="left:114px;top:529px"></div>
<div class="block" style="left:73px;top:549px;line-height:13px">
<b>Yellowtail</b><br><span class="dim">inside out roll with scallions (gf)</span><br><b>Spicy Tuna/ Salmon/ Yellowtail</b><br><span class="dim">spicy mayo</span><br><b>California</b><br><span class="dim">crab meat, cucumber and avocado (gf)</span><br><b>Vegetable</b><br><span class="dim">avocado, cucumber, asparagus and</span><br><span class="dim">pickled reddish (gf)</span><br><b>Spider</b><br><span class="dim">soft shell crab and avocado with</span><br><span class="dim">eel sauce</span><br><b>Shrimp Tempura</b><br><span class="dim">deep fried tempura shrimp and eel sauce</span><br><b>Alaskan</b><br><span class="dim">salmon and avocado (gf)</span>
</div>

<div class="orn" role="img" aria-label="leaf flourish divider" style="left:114px;top:785px"></div>
<div class="head" style="left:159px;top:798px">SEAFOOD PLATTERS (gf)</div>
<div class="orn" role="img" aria-label="leaf flourish divider" style="left:114px;top:819px"></div>
<div class="block" style="left:74px;top:842px;line-height:16px">Shrimp, Oysters, Clams,<br>Lobster and Crab</div>
<div class="block" style="left:74px;top:883px"><i class="em">Large or Colossal</i></div>

<div class="box" style="left:259px;top:323px;width:280px;height:113px">
  <div class="head" style="top:11px">SUSHI PLATTERS</div>
  <div class="block" style="left:10px;top:34px"><b>Small:</b>&nbsp; Five Pieces assorted sushi, nine pieces sashimi,<br><span style="padding-left:40px">spicy tuna roll (gf)</span><br><b>Large:</b>&nbsp; Eight Pieces assorted sushi,<br><span style="padding-left:40px">eighteen pieces of sashimi, alaskan roll,</span><br><span style="padding-left:40px">rainbow roll (gf)</span></div>
</div>

<div class="orn" role="img" aria-label="leaf flourish divider" style="left:360px;top:452px"></div>
<div class="head" style="left:406px;top:464px">SPECIAL ROLLS</div>
<div class="orn" role="img" aria-label="leaf flourish divider" style="left:360px;top:486px"></div>
<div class="block" style="left:272px;top:501px">
<div class="hang"><b>The Harbor</b>&nbsp; Tuna, salmon, yellowtail, avocado,<br>spicy mayo, soy bean paper</div>
<div class="hang"><b>King Crab Rainbow</b>&nbsp; King crab, avocado, cucumbers,<br>assorted fish on top</div>
<div class="hang"><b>Empress</b>&nbsp; Shrimp tempura, spicy tuna on top, eel sauce,<br>spicy mayo</div>
<div class="hang"><b>Spicy Girl</b>&nbsp; Spicy crunchy crab meat, cucumber,<br>shrimp on top</div>
<div class="hang"><b>Dragon</b>&nbsp; Eel, cucumber, avocado, and tobiko on top,<br>eel sauce</div>
<div class="hang"><b>Yummy</b>&nbsp; Spicy crunchy salmon, avocado, mango and<br>salmon on top</div>
<div class="hang"><b>No. 9</b>&nbsp; Shrimp Tempura, avocado, kani, spicy mayo,<br>tobiko</div>
<div class="hang"><b>Sunrise Roll</b>&nbsp; Spicy crunchy tuna and avocado,<br>spicy crunchy salmon on top</div>
</div>

<div class="orn" role="img" aria-label="leaf flourish divider" style="left:360px;top:736px"></div>
<div class="head" style="left:406px;top:749px">SEAFOOD RAW BAR</div>
<div class="orn" role="img" aria-label="leaf flourish divider" style="left:360px;top:770px"></div>
<div class="block" style="left:272px;top:788px">Lobster Cocktail<br>Shrimp Cocktail<br>Clams on the Half Shell</div>
<div class="block" style="left:409px;top:788px">Oysters on the Half Shell<br>Colossal Crab Cocktail</div>

<div class="box" style="left:272px;top:843px;width:254px;height:65px">
  <div class="block" style="left:0;right:0;top:11px;text-align:center"><i class="em">Raw Bar Plate for One:</i></div>
  <div class="block dim" style="left:10px;top:32px">Two Shrimp, Half of a One Pound Lobster, Two Clams,<br>One East Coast Oyster, One West Coast Oyster</div>
</div>

<!-- RIGHT PAGE -->
<div class="orn" role="img" aria-label="leaf flourish divider" style="left:717px;top:298px"></div>
<div class="head" style="left:763px;top:310px">APPS</div>
<div class="orn" role="img" aria-label="leaf flourish divider" style="left:717px;top:329px"></div>
<div class="block" style="left:661px;top:345px">
<div class="hang"><b>BAO Bun</b>&nbsp; hoisin bbq pancetta cut pork<br>loin, crispy onions, micro mint</div>
<div><b>Five Spice Crispy Popcorn Crusted</b><br><b>Prawns (2)</b>&nbsp; classic burre blanc</div>
<div class="hang"><b>Jumbo Lump Crab</b>&nbsp; citrus miso drizzle,<br>spring pea puree, micro greens</div>
<div class="hang"><b>Crispy Wonton Napoleon</b>&nbsp; cucumber<br>gallete, ahi tuna, jumbo lump crab<br>meat, wasabi aioli, shoestring wontons</div>
<div class="hang"><b>PEI Mussels</b>&nbsp; charred artichoke hearts,<br>blistered heirloom tomatoes,<br>garlic white wine broth</div>
<div><b>New Zealand or Domestic Small Eye</b><br><b>Lamb Chop (1)</b> crispy porcini risotto cake</div>
</div>

<div class="orn" role="img" aria-label="leaf flourish divider" style="left:717px;top:547px"></div>
<div class="head" style="left:763px;top:560px">ENTREES</div>
<div class="orn" role="img" aria-label="leaf flourish divider" style="left:717px;top:580px"></div>
<div class="block" style="left:661px;top:598px;line-height:13px">
<b>Pan Roasted Miso Glazed Black Cod</b><br><span class="dim">green tea noodle stir fry, Napa cabbage, carrot,</span><br><span class="dim">Japanese eggplant</span><br><b>Pan Seared Striped Bass</b><br><span class="dim">lobster succotash in a tomato saffron broth</span><br><b>E.V.O.O. Salted / Grilled Swordfish</b><br><span class="dim">sun dried tomato, olive and caper tapenade,</span><br><span class="dim">over basmati rice</span><br><b>Grilled Half Chicken</b><br><span class="dim">sun dried tomato and basil Israeli cous-cous,</span><br><span class="dim">pan au jus</span><br><b>Roasted Fresh Caviatelle Ratatoille</b><br><span class="dim">vegetable broth</span><br><b>Lobster Cartoccio</b><br><span class="dim">shrimp, mussels, clams, fresh herb tomato broth,</span><br><span class="dim">tossed with bucatini</span><br><b>Charred Artichoke Hearts</b><br><span class="dim">heirloom tomatoes, caper berries, spring onions,</span><br><span class="dim">fresh basil, white wine reduction over forbidden</span><br><span class="dim">rice (gf)</span><br><b>Mediterranean Grilled Veggie Plate</b><br><span class="dim">artichoke hearts, Japanese eggplant,</span><br><span class="dim">green &amp; white asparagus, seared heirloom</span><br><span class="dim">tomatoes, roasted baby carrots, cauliflower rice,</span><br><span class="dim">evoo &amp; fig drizzle (gf)</span>
</div>

<div class="box" style="left:888px;top:296px;width:161px;height:38px">
  <div class="head" style="top:3px;font-size:13px">DESSERTS</div>
  <div class="block dim" style="left:0;right:0;top:20px;text-align:center">T.B.D. - separate menu</div>
</div>

<div class="orn" role="img" aria-label="leaf flourish divider" style="left:956px;top:346px"></div>
<div class="head" style="left:1002px;top:358px">SALADS</div>
<div class="orn" role="img" aria-label="leaf flourish divider" style="left:956px;top:378px"></div>
<div class="block" style="left:890px;top:398px;line-height:13px">
<b>Classic Wedge</b><br><span class="dim">bleu cheese, bacon lardons, heirloom tomatoes</span><br><b>Mixed Baby Greens</b><br><span class="dim">heirloom tomatoes, cucumber, red onion,</span><br><span class="dim">dijon vinaigrette</span><br><b>Tabulleh</b><br><span class="dim">buckwheat grain, fresh mint, tomato concasse,</span><br><span class="dim">cucumber, parsley, fresh squeezed lemon, EVOO.,</span><br><span class="dim">salt and pepper</span><br><b>Spinach Salad</b><br><span class="dim">green apple, feta, currants,</span><br><span class="dim">with per-simmons vinaigrette</span><br><b>Kale Caesar</b><br><span class="dim">homemade cacio e'peppe dressing, pecorino and</span><br><span class="dim">parmesan cheese, toasted croutons</span><br><b>Tomato Mozzarella Salad/ Burratta</b>
</div>

<div class="box" style="left:888px;top:615px;width:234px;height:86px">
  <div class="head" style="top:10px">USDA PRIME STEAKS (gf)</div>
  <div class="block dim" style="left:5px;top:39px">10 Oz Filet<br>24 oz Boneless Ribeye<br>14 or 16 oz New York Strip</div>
  <div class="block dim" style="left:135px;top:39px">36 oz Bone in Rib Eye<br>Berkshire Pork Chop</div>
</div>

<div class="box" style="left:888px;top:708px;width:234px;height:78px">
  <div class="head" style="top:10px">SAUCES</div>
  <div class="block dim" style="left:5px;top:31px">Cabernet Demi Glaz<br>Gorganzola Brulle Cream<br>Truffled Wild Mushroom Ragu</div>
  <div class="block dim" style="left:141px;top:31px">Horseradish Cream<br>House Steak Sauce</div>
</div>

<div class="box" style="left:888px;top:794px;width:234px;height:125px">
  <div class="head" style="top:8px">SIDES</div>
  <div class="block dim" style="left:5px;top:30px">Mashed Idaho Potatoes<br>Roasted Peanut Potatoes<br>Creamed Spinach<br>Saut&eacute;ed Spinach<br>Sweet Potato Steak Fries<br>Bacon, Sweet Corn,<br>Caramelized Vidalia Onion fingerling potatoes</div>
  <div class="block dim" style="left:141px;top:30px">French Beans<br>Israeli Cous Cous<br>Corn Skillet<br>Grilled Asparagus</div>
</div>
</body>
</html>
```